Business Cards for a Junk Removal Company

Hello,
We are looking to have business cards designed that are simple, bold, easy to read, and right to the point. Please see the attachments for our logo files. We want the card to be yellow on both sides ( Color code Yellow: #FFE01B). The logo text font is (Rockstar Extra Bold) and this is also in the files attached. Please make the text black for the logo. On the back side of the card, you can use white and black for text. Thank you in advance for your hard work!

Front of card-
Harbor Haul Away (logo)
Back of card-
Harbor Haul Away
Donate - Recycle - Dispose
555-271-8093
www.harborhaulaway.example
info@harborhaulaway.example

Industry/Entity Type

Junk removal

Contact Information for Business Card

FRONT OF CARD- Harbor Haul Away (logo) BACK OF CARD- Harbor Haul Away Donate - Recycle - Dispose 555-271-8093 www.harborhaulaway.example info@harborhaulaway.example

Font styles to use
Other font styles liked:
• Rockstar Extra Bold

Colors
FFF300
FFF600
FEFA6F
FFFEC7
FFFEE8

Requirements
Must have
• Must have color code Yellow: #FFE01B for the background of front and back of the card

```html
<!DOCTYPE html>
<html lang="en">
<head>
<meta charset="utf-8">
<title>Harbor Haul Away – Business Cards</title>
<link rel="stylesheet" href="https://fonts.googleapis.com/css2?family=Anton&display=swap">
<style>
  :root {
    --backdrop: #2b2b2b;
    --card-yellow: #dcc23a;
    --ink: #111111;
    --card-shadow: rgba(0, 0, 0, 0.45);
  }
  html, body {
    margin: 0;
    padding: 0;
    overflow: hidden;
  }
  body {
    width: 1200px;
    height: 1138px;
    background: var(--backdrop);
    position: relative;
    font-family: "Anton", "Impact", sans-serif;
    color: var(--ink);
  }
  .card {
    position: absolute;
    background: var(--card-yellow);
    border-radius: 16px;
    box-shadow: 0 4px 10px var(--card-shadow);
  }
  .card-front {
    left: 274px;
    top: 186px;
    width: 624px;
    height: 376px;
  }
  .card-back {
    left: 276px;
    top: 608px;
    width: 618px;
    height: 374px;
  }
  .front-name {
    position: absolute;
    left: 0;
    right: 0;
    top: 150px;
    text-align: center;
    font-size: 66px;
    line-height: 1;
    letter-spacing: 1px;
    text-transform: uppercase;
  }
  .back-name {
    position: absolute;
    left: 78px;
    top: 32px;
    height: 312px;
    writing-mode: vertical-rl;
    transform: rotate(180deg);
    font-size: 44px;
    line-height: 1;
    letter-spacing: 1px;
    text-align: center;
    text-transform: uppercase;
  }
  .contact-list {
    position: absolute;
    left: 246px;
    top: 128px;
    margin: 0;
    padding: 0;
    list-style: none;
  }
  .contact-item {
    display: flex;
    align-items: center;
    gap: 10px;
    height: 25px;
    font-size: 16px;
    text-transform: uppercase;
    letter-spacing: 0.2px;
  }
  .contact-icon {
    width: 16px;
    height: 14px;
    flex: none;
  }
  .tagline {
    position: absolute;
    left: 246px;
    top: 222px;
    margin: 0;
    font-size: 16px;
    text-transform: uppercase;
    letter-spacing: 0.2px;
  }
</style>
</head>
<body>

  <section class="card card-front" aria-label="Card front">
    <div class="front-name">Harbor Haul Away</div>
  </section>

  <section class="card card-back" aria-label="Card back">
    <div class="back-name">Harbor Haul Away</div>

    <ul class="contact-list">
      <li class="contact-item">
        <svg class="contact-icon" viewBox="0 0 16 14" aria-hidden="true">
          <path d="M1 5c0-2 3-3.5 7-3.5S15 3 15 5l-3 1-1-2H5L4 6 1 5z" fill="var(--ink)"/>
          <path d="M4 7h8l2 6H2z" fill="var(--ink)"/>
        </svg>
        <span>555-271-8093</span>
      </li>
      <li class="contact-item">
        <svg class="contact-icon" viewBox="0 0 16 14" aria-hidden="true">
          <rect x="1" y="2" width="14" height="10" fill="var(--ink)"/>
          <path d="M1.5 2.5 8 8l6.5-5.5M1.5 11.5 6 7m8.5 4.5L10 7" stroke="var(--card-yellow)" stroke-width="1" fill="none"/>
        </svg>
        <span>info@harborhaulaway.example</span>
      </li>
      <li class="contact-item">
        <svg class="contact-icon" viewBox="0 0 16 14" aria-hidden="true">
          <circle cx="8" cy="7" r="6" fill="var(--ink)"/>
          <g stroke="var(--card-yellow)" stroke-width="0.8" fill="none">
            <ellipse cx="8" cy="7" rx="2.5" ry="6"/>
            <path d="M2 7h12M3 4h10M3 10h10"/>
          </g>
        </svg>
        <span>www.harborhaulaway.example</span>
      </li>
    </ul>

    <p class="tagline">Donate - Recycle - Dispose</p>
  </section>

</body>
</html>
```